Private Learning Centre in Singapore needs a flyer design

We need a flyer design for our upcoming education fair and also able to use it for day to day purpose. The aim is to attract parents, students to enrol for classes by offering them free trial class/assessment. 2 sided flyer with the front page as the logo only and details on the other page. We would like to see a final design in blue, white and it should be curious and attractive enough not to allow customers to throw it away once they received it.

Education

```html
<!DOCTYPE html>
<html lang="en">
<head>
<meta charset="UTF-8">
<title>Bright Path Academy – Flyer</title>
<link href="https://fonts.googleapis.com/css2?family=Arvo:wght@400;700&display=swap" rel="stylesheet">
<style>
  :root {
    --brand-blue: #4a5ba6;
    --accent-cyan: #29abe2;
    --paper: #ffffff;
    --backdrop: #e9eaee;
    --photo-light: #e8eef6;
    --photo-mid: #c9d3e2;
    --photo-warm: #d9c3a8;
    --social-tint: rgba(255, 255, 255, 0.3);
  }
  * { margin: 0; padding: 0; box-sizing: border-box; }
  html, body { width: 1200px; height: 800px; overflow: hidden; }
  body {
    background: var(--backdrop);
    font-family: "Arvo", Georgia, serif;
    position: relative;
  }
  .flyer {
    position: absolute;
    top: 117px;
    width: 400px;
    height: 566px;
    overflow: hidden;
    box-shadow: 0 8px 24px rgba(0, 0, 0, 0.18);
  }

  /* Front side */
  .flyer-front { left: 180px; background: var(--brand-blue); color: var(--paper); }
  .front-stripe {
    position: absolute; left: 0; top: 150px;
    width: 100%; height: 8px; background: var(--accent-cyan);
  }
  .front-name {
    position: absolute; left: 0; top: 192px; width: 100%;
    text-align: center; font-size: 30px; font-weight: 400;
    letter-spacing: 3px; line-height: 1.35;
  }
  .front-offer {
    position: absolute; left: 0; top: 318px; width: 100%;
    text-align: center; font-size: 34px; font-weight: 700; line-height: 1.25;
  }
  .front-website {
    position: absolute; left: 0; top: 462px; width: 100%;
    text-align: center; font-size: 22px;
  }

  /* Back side */
  .flyer-back { left: 620px; background: var(--paper); }
  .back-tagline {
    position: absolute; left: 28px; top: 34px;
    color: var(--brand-blue); font-size: 17px; line-height: 1.3;
  }
  .back-brand {
    position: absolute; right: 22px; top: 82px; width: 110px;
    color: var(--brand-blue); font-size: 12px; line-height: 1.4;
    text-align: center; letter-spacing: 1px;
  }
  .back-photo {
    position: absolute; left: 0; top: 150px; width: 100%; height: 176px;
    background: linear-gradient(100deg, var(--photo-warm) 0%, var(--photo-light) 35%, var(--photo-mid) 70%, var(--photo-light) 100%);
  }
  .back-stripe {
    position: absolute; left: 0; top: 326px; width: 100%; height: 8px;
    background: var(--accent-cyan);
  }
  .back-panel {
    position: absolute; left: 0; top: 334px; width: 100%; bottom: 0;
    background: var(--brand-blue); color: var(--paper);
  }
  .back-intro {
    margin: 20px 30px 0; font-size: 11.5px; line-height: 1.55; text-align: justify;
  }
  .back-contact {
    position: absolute; left: 30px; bottom: 20px; width: 300px;
    font-style: normal; font-size: 13px; font-weight: 700;
    line-height: 1.45; text-align: center;
  }
  .back-social {
    position: absolute; right: 24px; bottom: 22px;
    width: 30px; height: 30px; border-radius: 50%; background: var(--social-tint);
  }
</style>
</head>
<body>

  <section class="flyer flyer-front">
    <div class="front-stripe"></div>
    <p class="front-name">BRIGHT PATH<br>ACADEMY</p>
    <p class="front-offer">FREE TRIAL<br>CLASS</p>
    <p class="front-website">www.brightpathacademy.com</p>
  </section>

  <section class="flyer flyer-back">
    <p class="back-tagline">Inspiring young minds.<br>Empowering young hearts.</p>
    <p class="back-brand">BRIGHT PATH<br>ACADEMY</p>
    <div class="back-photo" role="img" aria-label="Photo of a teacher in front of a classroom with students raising their hands"></div>
    <div class="back-stripe"></div>
    <div class="back-panel">
      <p class="back-intro">Bright Path Academy is where you can develop academic and life skills. Our teachers are the heartbeat of the business. They inspire and nurture students, helping them surpass their expectations. We cover English, Mathematics and Science from Primary and Secondary Levels.</p>
      <address class="back-contact">
        <div>Bright Path Academy</div>
        <div>418 Marine Parade Road S449281</div>
        <div>6215 4870</div>
        <div>enquire@brightpathacademy.com</div>
      </address>
      <span class="back-social" aria-hidden="true"></span>
    </div>
  </section>

</body>
</html>
```